Candle company needs a label for candle

Looking for a designer to create my candle label. I am going to attach a few pictures of my vision for the label as well as my Company Logo and jar I have puchased. I'm going for the modern rustic feel but you are the designer and have full trust in your abilities. The label is going to be printed on Kraft paper (2x3) so looking for the font to be black. The candle label MUST include the following information:
Wick Harbor Co.
NO. 01: Eucalyptus + Spearmint
Handmade In NJ
Soy Wax
9oz

Industry/Entity Type

Candle Industry

Colors

Designer to choose colors to be used in the design.

Requirements
Should not have
• Any images

```html
<!DOCTYPE html>
<html lang="en">
<head>
<meta charset="UTF-8">
<title>Wick Harbor Co. — No. 01 Label</title>
<link href="https://fonts.googleapis.com/css2?family=Bebas+Neue&display=swap" rel="stylesheet">
<style>
  :root {
    --page: #ffffff;
    --kraft: #d9b88f;
    --kraft-dark: #cfae84;
    --ink: #111111;
  }
  * { margin: 0; padding: 0; box-sizing: border-box; }
  html, body {
    width: 1079px;
    height: 1200px;
    overflow: hidden;
    background: var(--page);
  }
  .canvas {
    position: relative;
    width: 1079px;
    height: 1200px;
  }
  .label {
    position: absolute;
    left: 40px;
    top: 266px;
    width: 1000px;
    height: 667px;
    border-radius: 22px;
    background: radial-gradient(ellipse at 40% 40%, var(--kraft) 0%, var(--kraft-dark) 100%);
    font-family: "Bebas Neue", sans-serif;
    color: var(--ink);
  }
  .label-frame {
    position: absolute;
    inset: 28px;
    border: 3px solid var(--ink);
    border-radius: 12px;
  }
  .brand {
    position: absolute;
    top: 110px;
    left: 0;
    right: 0;
    display: flex;
    justify-content: center;
    align-items: center;
    gap: 22px;
  }
  .brand-square {
    width: 22px;
    height: 22px;
    background: var(--ink);
  }
  .brand-name {
    font-size: 64px;
    line-height: 0.95;
    letter-spacing: 10px;
    text-align: left;
  }
  .scent-name {
    position: absolute;
    top: 380px;
    left: 0;
    right: 0;
    text-align: center;
    font-size: 72px;
    line-height: 1;
    letter-spacing: -0.5px;
  }
  .divider {
    position: absolute;
    top: 462px;
    left: 106px;
    right: 110px;
    border-top: 2px dashed var(--ink);
  }
  .details {
    position: absolute;
    top: 462px;
    left: 0;
    right: 0;
    display: flex;
    justify-content: center;
    align-items: center;
    height: 72px;
    font-size: 38px;
    letter-spacing: 4px;
  }
  .details-sep {
    width: 2px;
    height: 72px;
    background: var(--ink);
    margin: 0 30px;
  }
  .weight {
    position: absolute;
    top: 555px;
    left: 0;
    right: 0;
    text-align: center;
    font-size: 38px;
    letter-spacing: 4px;
  }
</style>
</head>
<body>
  <main class="canvas">
    <section class="label">
      <div class="label-frame"></div>

      <div class="brand">
        <span class="brand-square"></span>
        <p class="brand-name">WICK<br>HARBOR CO.</p>
      </div>

      <h1 class="scent-name">NO. 01: EUCALYPTUS + SPEARMINT</h1>
      <div class="divider"></div>

      <div class="details">
        <span class="origin">HANDMADE IN NJ</span>
        <span class="details-sep"></span>
        <span class="wax">100% SOY WAX</span>
      </div>

      <p class="weight">9OZ</p>
    </section>
  </main>
</body>
</html>
```